Web Design Project for SEARCH ENGINE !

We need a website design for torrents search engine.

The Website will be www.Qurvex.com

Qurvex is a a search engine for torrents.
Qurvex search and index torrents results from all torrents sites.

We will need:
Logo
WebSite Design
slogen (optional)

we need only PSDs - no codded pages are needed !

Design to the following screen Size & resolution: 1024 x 768

***PLEASE DOWNLOAD ATTACHED FILE !

```html
<!DOCTYPE html>
<html lang="en">
<head>
<meta charset="utf-8">
<title>Qurvex – Torrents Search Engine</title>
<link rel="stylesheet" href="https://fonts.googleapis.com/css2?family=Jost:wght@400;500&family=Source+Sans+3:wght@400&display=swap">
<style>
  :root {
    --green: #2bb540;
    --ink: #333333;
    --grey-logo: #6b6b6b;
    --bar-top: #3a3a3a;
    --bar-bottom: #141414;
    --nav-text: #ffffff;
    --page-bg: #ffffff;
    --outer-bg: #d9d9d9;
    --frame: #c4c4c4;
    --media-a: #4d5b68;
    --media-b: #3a4654;
  }
  * { margin: 0; padding: 0; box-sizing: border-box; }
  html, body { width: 1200px; height: 896px; overflow: hidden; }
  body {
    background: var(--outer-bg);
    font-family: "Source Sans 3", "Helvetica Neue", Arial, sans-serif;
    color: var(--ink);
    position: relative;
  }
  .page {
    position: absolute; left: 7px; top: 0; width: 1186px; height: 896px;
    background: linear-gradient(180deg, #eeeeee 0%, var(--page-bg) 18%, var(--page-bg) 70%, #ececec 100%);
  }
  .bar {
    position: absolute; left: 7px; width: 1186px;
    background: linear-gradient(180deg, var(--bar-top), var(--bar-bottom));
  }
  .top-bar { top: 4px; height: 34px; }
  .main-nav {
    position: absolute; left: 254px; top: 0; height: 34px;
    display: flex; align-items: center;
    font-family: "Jost", "Futura", sans-serif; font-size: 15px; color: var(--nav-text);
  }
  .main-nav a { color: inherit; text-decoration: none; }
  .main-nav a.current { color: var(--green); }
  .main-nav .sep { margin: 0 10px; }
  .lang-select {
    position: absolute; left: 867px; top: 6px; width: 71px; height: 23px;
    background: var(--green); color: #fff;
    font-family: "Jost", sans-serif; font-size: 12px;
    display: flex; align-items: center; padding-left: 8px;
  }
  .lang-select::after {
    content: ""; position: absolute; right: 9px; top: 9px;
    border-left: 4px solid transparent; border-right: 4px solid transparent; border-top: 6px solid #fff;
  }
  .brand {
    position: absolute; left: 0; top: 62px; width: 1200px; text-align: center;
    font-family: "Jost", sans-serif;
  }
  .brand-name {
    display: inline-flex; align-items: center; gap: 8px;
    font-size: 54px; font-weight: 500; color: var(--grey-logo); line-height: 58px;
  }
  .brand-dot { width: 40px; height: 40px; border-radius: 50%; background: var(--green); }
  .brand-tag { font-size: 14px; color: var(--grey-logo); letter-spacing: 0.5px; margin-top: 2px; }
  .hero-media {
    position: absolute; left: 246px; top: 189px; width: 336px; height: 246px;
    border: 6px solid var(--frame);
    background: linear-gradient(160deg, var(--media-a), var(--media-b));
  }
  .welcome { position: absolute; left: 606px; top: 186px; width: 352px; }
  .welcome h1 {
    font-family: "Jost", sans-serif; font-weight: 400; font-size: 34px; line-height: 42px;
    letter-spacing: -0.5px; color: var(--ink); text-transform: uppercase; white-space: nowrap;
  }
  .welcome h2 {
    font-family: "Jost", sans-serif; font-weight: 400; font-size: 20.5px; line-height: 26px;
    color: var(--green); white-space: nowrap;
  }
  .welcome p { font-size: 13px; line-height: 16.8px; margin-top: 6px; white-space: nowrap; }
  .body-copy {
    position: absolute; left: 246px; width: 710px;
    font-size: 13.3px; line-height: 16.8px; white-space: nowrap;
  }
  .copy-1 { top: 459px; }
  .copy-2 { top: 553px; }
  .copy-3 { top: 640px; }
  .signin-cta {
    position: absolute; left: 823px; top: 735px; width: 130px; height: 44px;
    background: var(--green); color: #fff; text-decoration: none;
    font-family: "Jost", sans-serif; font-size: 16px;
    display: flex; align-items: center; justify-content: center;
  }
  .social { position: absolute; left: 536px; top: 799px; display: flex; gap: 20px; }
  .social a { width: 29px; height: 29px; border-radius: 3px; display: block; }
  .social .feed { background: #e0762a; }
  .social .micro { background: #8fd0ea; }
  .social .network { background: #3b5c9a; }
  .bottom-bar { top: 853px; height: 37px; }
  .legal {
    position: absolute; left: 0; top: 0; width: 100%; height: 37px;
    display: flex; align-items: center; justify-content: center; white-space: pre;
    font-family: "Jost", sans-serif; font-size: 12.5px; color: #fff; text-transform: uppercase;
  }
  .legal a { color: var(--green); text-decoration: none; }
</style>
</head>
<body>
  <div class="page"></div>

  <header class="bar top-bar">
    <nav class="main-nav">
      <a class="current" href="#">HOME</a><span class="sep">|</span>
      <a href="#">ABOUT US</a><span class="sep">|</span>
      <a href="#">TORRENT SEARCH</a><span class="sep">|</span>
      <a href="#">CATEGORIES</a><span class="sep">|</span>
      <a href="#">HELP</a><span class="sep">|</span>
      <a href="#">LOGIN</a><span class="sep">|</span>
      <a href="#">SIGNIN</a>
    </nav>
    <div class="lang-select">English</div>
  </header>

  <div class="brand">
    <div class="brand-name"><span class="brand-dot"></span>Qurvex</div>
    <div class="brand-tag">TORRENTS SEARCH ENGINE</div>
  </div>

  <div class="hero-media" role="img" aria-label="Collage of colourful media thumbnails: films, games, music and software"></div>

  <section class="welcome">
    <h1>Welcome to Qurvex<br>Search,Get,Enjoy</h1>
    <h2>Movies, Games, Music, Software, etc.</h2>
    <p>Lorem ipsum dolor sit amet, consetetur sadipscing elitr, sed<br>
    nonumy eirmod tempor invidunt ut labore et dolore magna<br>
    aliquyam erat, sed diam voluptua. At vero eos et accusam et<br>
    duo dolores et ea rebum. Stet clita kasd gubergren, no sea<br>
    sanctus est Lorem ipsum dolor sit amet. Lorem ipsum dolor<br>
    consetetur sadipscing elitr, sed diam nonumy eirmod<br>
    invidunt ut labore et dolore magna aliquyam erat, sed diam<br>
    At vero eos et accusam et justo duo dolores et ea</p>
  </section>

  <p class="body-copy copy-1">Lorem ipsum dolor sit amet, consetetur sadipscing elitr, sed diam nonumy eirmod tempor invidunt ut labore et dolore<br>
  magna erat, sed diam voluptua. At vero eos et accusam et justo duo dolores et ea rebum. Stet clita kasd gubergren,<br>
  no sea takimata Lorem ipsum dolor sit amet. Lorem ipsum dolor sit amet, consetetur sadipscing elitr, sed diam nonumy<br>
  eirmod tempor et dolore magna aliquyam erat, sed diam voluptua. At vero eos et accusam et justo duo dolores et ea</p>
  <p class="body-copy copy-2">Lorem ipsum dolor sit amet, consetetur sadipscing elitr, sed diam nonumy eirmod tempor invidunt ut labore et dolore<br>
  magna erat, sed diam voluptua. At vero eos et accusam et justo duo dolores et ea rebum. Stet clita kasd gubergren,<br>
  no sea takimata Lorem ipsum dolor sit amet. Lorem ipsum dolor sit amet, consetetur sadipscing elitr, sed diam nonumy<br>
  eirmod tempor et dolore magna aliquyam erat, sed diam voluptua. At vero eos et accusam et justo duo dolores et ea</p>
  <p class="body-copy copy-3">Lorem ipsum dolor sit amet, consetetur sadipscing elitr, sed diam nonumy eirmod tempor invidunt ut labore et dolore<br>
  magna erat, sed diam voluptua. At vero eos et accusam et justo duo dolores et ea rebum. Stet clita kasd gubergren,<br>
  no sea takimata Lorem ipsum dolor sit amet. Lorem ipsum dolor sit amet, consetetur sadipscing elitr, sed diam nonumy<br>
  eirmod tempor et dolore magna aliquyam erat, sed diam voluptua. At vero eos et accusam et justo duo dolores et ea</p>

  <a class="signin-cta" href="#">SIGNIN NOW</a>

  <div class="social">
    <a class="feed" href="#" aria-label="News feed"></a>
    <a class="micro" href="#" aria-label="Short updates"></a>
    <a class="network" href="#" aria-label="Social network"></a>
  </div>

  <footer class="bar bottom-bar">
    <div class="legal">Copyright © 2011 Qurvex. Use of this website constitutes acceptance of our <a href="#">User Agreement</a> and <a href="#">Privacy Policy</a>.</div>
  </footer>
</body>
</html>
```